Interior Stylist business card design needed

I need a business card for my new company in Sydney called "Pip Dunstane Designs". The business offers an interior styling and colour consultancy. My clients are generally not very design savvy (hence why they use me) and can range from being quite conservative to really wanting something "out there". They can be looking for a budget makeover or something more expensive / substantial. I'd like my business card design to be stylish (but not overly formal). I certainly don't want it to be conservative. I'd like it to stand out a bit! I don't really have any aversion to particular colours and I don't have a logo as such - my business name is really all I have.

Target Market(s)

As above - home owners, ranging from conservative to modern

Industry/Entity Type

Conservative

Contact Information for Business Card

Pip Dunstane Designs
Colour consultancy and interior styling
ph: 0417 382 605
email: pipdunstane@harvolink.net.au

Requirements
Should not have
• Old fashioned writing or motifs. No Times Roman font!!

```html
<!DOCTYPE html>
<html lang="en">
<head>
<meta charset="utf-8">
<title>Pip Dunstane Designs – Business Card</title>
<link rel="stylesheet" href="https://fonts.googleapis.com/css2?family=Josefin+Sans:wght@600&display=swap">
<style>
  :root {
    --page-bg: #070908;
    --card-light: #39322f;
    --card-dark: #141414;
    --band-light: #dcdcdc;
    --band-brown: #774c21;
    --swatch-green: #a6e25e;
    --swatch-violet: #e867e8;
    --swatch-orange: #eba86a;
    --swatch-cyan: #86e8e8;
    --swatch-rose: #e766a2;
    --swatch-shade: rgba(0, 0, 0, 0.55);
    --ink-white: #ffffff;
  }
  * { margin: 0; padding: 0; box-sizing: border-box; }
  html, body {
    width: 1200px;
    height: 720px;
    overflow: hidden;
    background: var(--page-bg);
  }
  .card {
    position: absolute;
    left: 40px;
    top: 40px;
    width: 1120px;
    height: 640px;
    border-radius: 48px;
    overflow: hidden;
  }
  .card-texture {
    position: absolute;
    inset: 0;
    background: radial-gradient(ellipse at 50% 45%, var(--card-light) 0%, #262322 45%, var(--card-dark) 100%);
  }
  .top-band {
    position: absolute;
    left: 0;
    top: 74px;
    width: 100%;
    height: 45px;
    background: var(--band-light);
  }
  .swatch {
    position: absolute;
    top: 99px;
    width: 179px;
    height: 39px;
  }
  .swatch::after {
    content: "";
    position: absolute;
    left: 0;
    top: 20px;
    width: 100%;
    height: 19px;
    background: var(--swatch-shade);
  }
  .swatch--green  { left: 40px;  background: var(--swatch-green); }
  .swatch--violet { left: 255px; background: var(--swatch-violet); }
  .swatch--orange { left: 470px; background: var(--swatch-orange); }
  .swatch--cyan   { left: 685px; background: var(--swatch-cyan); }
  .swatch--rose   { left: 900px; background: var(--swatch-rose); }
  .bottom-band {
    position: absolute;
    left: 0;
    top: 559px;
    width: 100%;
    height: 41px;
    background: var(--band-brown);
  }
  .brand {
    position: absolute;
    left: 0;
    top: 405px;
    width: 100%;
    display: flex;
    align-items: center;
    justify-content: center;
    gap: 22px;
  }
  .brand-mark {
    width: 62px;
    height: 62px;
    border-radius: 50%;
    background: var(--ink-white);
    flex: none;
  }
  .brand-name {
    font-family: "Josefin Sans", "Century Gothic", sans-serif;
    font-weight: 600;
    font-size: 42px;
    line-height: 1;
    color: var(--ink-white);
    letter-spacing: 1px;
    padding-top: 8px;
  }
</style>
</head>
<body>
  <main class="card">
    <div class="card-texture" role="img" aria-label="Dark honeycomb texture background with a soft central glow"></div>
    <div class="top-band"></div>
    <div class="swatch swatch--green"></div>
    <div class="swatch swatch--violet"></div>
    <div class="swatch swatch--orange"></div>
    <div class="swatch swatch--cyan"></div>
    <div class="swatch swatch--rose"></div>
    <div class="brand">
      <span class="brand-mark"></span>
      <h1 class="brand-name">Pip Dunstane Designs</h1>
    </div>
    <div class="bottom-band"></div>
  </main>
</body>
</html>
```